4th Generation Family Business Needs a New Card Design!

We are a family owned 4th Generation company. We are based in the Sydney, Australia area and we are desperately in need of a more modern and classy card. We are monumental masons who design, supply & erect lasting memorials throughout cemeteries in Sydney. Our customers are normally in a period of grieving. I have attached logo files that will need to be implemented on the card. Company was established 1935. Australian Owned and Operated. Card needs to be designed to PRINTLY.com specification.

Target Market(s)

Our target market is based upon people that a grieving for family members that have passed away. We also deal with alot of companies that own and operate cemeteries.

Industry/Entity Type

Business

Contact Information for Business Card

Oliver Brantley, Operations Manager, 0417552908, oliver@hollowaystoneworks.com.au
Martin Brantley, Director, 0431906627, martin@hollowaystoneworks.com.au
Phone # 02 9634 2258
Website: www.hollowaystoneworks.com.au
Address: Suite 17, 8 Calloway Lane, East Penrose, Sydney NSW 2290

Font styles to use
Serif
Decorative
Script

Requirements
Must have
• Would like to see the logo nicely implemented with a modern design. Embossed lettering would be a nice additive.

```html
<!DOCTYPE html>
<html lang="en">
<head>
<meta charset="UTF-8">
<title>Holloway Stoneworks — Business Card</title>
<link href="https://fonts.googleapis.com/css2?family=Cinzel:wght@400;600&family=Crimson+Text:wght@400;600&display=swap" rel="stylesheet">
<style>
  :root {
    --backdrop: #e6e6e4;
    --gold: #ebbb22;
    --gold-deep: #e3ad18;
    --paper: #ffffff;
    --ink: #2b2b2b;
    --ink-soft: #4a4a4a;
    --shadow: rgba(0, 0, 0, 0.18);
  }
  * { box-sizing: border-box; margin: 0; padding: 0; }
  html, body {
    width: 1200px;
    height: 1000px;
    overflow: hidden;
    background: var(--backdrop);
  }
  .canvas {
    width: 1200px;
    height: 1000px;
    display: flex;
    flex-direction: column;
    align-items: center;
    justify-content: center;
    gap: 60px;
  }
  .card {
    width: 700px;
    height: 400px;
    box-shadow: 0 10px 28px var(--shadow);
    position: relative;
  }
  /* Front */
  .card-front {
    background: linear-gradient(135deg, var(--gold) 0%, var(--gold-deep) 100%);
    display: flex;
    align-items: center;
    justify-content: center;
  }
  .brand-name {
    font-family: "Cinzel", serif;
    font-weight: 400;
    color: var(--paper);
    text-align: center;
    line-height: 1.1;
    letter-spacing: 3px;
  }
  .card-front .brand-name { font-size: 52px; }
  .card-front .brand-name span { display: block; font-size: 28px; letter-spacing: 6px; margin-top: 8px; }

  /* Back */
  .card-back {
    background: var(--paper);
    color: var(--ink);
    padding: 36px 56px;
  }
  .card-back .brand-name {
    color: var(--ink);
    font-size: 26px;
    letter-spacing: 2px;
  }
  .card-back .brand-name span { display: block; font-size: 13px; letter-spacing: 4px; margin-top: 4px; }
  .contacts {
    display: flex;
    justify-content: center;
    margin-top: 34px;
  }
  .person {
    width: 260px;
    font-family: "Crimson Text", serif;
    font-size: 15px;
    line-height: 1.45;
    color: var(--ink-soft);
  }
  .person-left { text-align: right; padding-right: 26px; }
  .person-right { text-align: left; padding-left: 26px; }
  .divider {
    width: 2px;
    background: var(--gold);
    align-self: stretch;
  }
  .person-name {
    font-family: "Cinzel", serif;
    font-weight: 600;
    font-size: 19px;
    color: var(--ink);
    letter-spacing: 1px;
  }
  .person-role { font-weight: 600; color: var(--ink); margin-bottom: 10px; }
  .company-details {
    font-family: "Crimson Text", serif;
    font-size: 15px;
    line-height: 1.45;
    color: var(--ink-soft);
    position: absolute;
    left: 56px;
    bottom: 34px;
  }
</style>
</head>
<body>
<main class="canvas">
  <section class="card card-front">
    <div class="brand-name">HOLLOWAY<span>STONEWORKS</span></div>
  </section>

  <section class="card card-back">
    <div class="brand-name">HOLLOWAY<span>STONEWORKS</span></div>
    <div class="contacts">
      <div class="person person-left">
        <div class="person-name">OLIVER BRANTLEY</div>
        <div class="person-role">Operation Manager</div>
        <div>0417552908</div>
        <div>oliver@hollowaystoneworks.com.au</div>
      </div>
      <div class="divider"></div>
      <div class="person person-right">
        <div class="person-name">MARTIN BRANTLEY</div>
        <div class="person-role">Director</div>
        <div>0431906627</div>
        <div>martin@hollowaystoneworks.com.au</div>
      </div>
    </div>
    <div class="company-details">
      <div>phone-02 9634 2258</div>
      <div>web-www.hollowaystoneworks.com.au</div>
      <div>address-Suite 17, 8 Calloway Lane, East Penrose, Sydney NSW 2290</div>
    </div>
  </section>
</main>
</body>
</html>
```